Patent Law

Need to develop a home page for a patent lawyer.

Colors should go with logo, blues...

Company Name- Corvel Tindry, PLLC

Company Overview-

I am an Intellectual Property Lawyer and focus on patents, copyrights, trademarks, & trade secrets. I work with small businesses and start ups in the chemical and biotech industries.

Why Us-

I am small firm that can provide large-firm service at a reasonable price. I also can charge flat-fees for entreprenuers in certain practice areas.

Services-
Intellectual Property
Patents
Copyrights
Trademarks
Trade secrets
Healthcare Compliance
Elder law
Wills
Trusts

Website we like-
http://www.quarnlowtide.example/ - within industry!!
http://www.vopperhask.example/
http://dulbrickovan.example/
http://thefernwoldguides.example/

Target Market(s)

My customers will be small business, specifically small start-up companies in the chemical and biotech arena.

Industry/Entity Type

Trade

Requirements
Must have
• Colors should go with logo, blues...

```html
<!DOCTYPE html>
<html lang="en">
<head>
<meta charset="utf-8">
<title>Corvel Tindry, PLLC — Intellectual Property Law</title>
<link rel="stylesheet" href="https://fonts.googleapis.com/css2?family=Open+Sans:wght@400;600;700&family=Roboto+Condensed:wght@400;700&family=Noto+Serif:wght@400&display=swap">
<style>
:root{
  --sky:#06a6e8;
  --sky-light:#5cc8f5;
  --navy:#394fa0;
  --slate:#677b85;
  --charcoal:#44525c;
  --ink:#222a30;
  --nav-grey:#5b6570;
  --nav-active:#1a6fc0;
  --page:#f4f2f3;
  --white:#ffffff;
  --black:#000000;
  --rule:#b5b5b5;
  --search-btn:#2d63b8;
  --link-pale:#a7dcf5;
}
*{box-sizing:border-box;margin:0;padding:0}
html,body{width:1200px;height:1169px;overflow:hidden}
body{background:var(--page);font-family:"Open Sans",Arial,sans-serif;color:var(--ink);position:relative}
a{text-decoration:none;color:inherit}

.site-header{position:absolute;left:0;top:0;width:1200px;height:204px;background:var(--white)}
.top-strip{position:absolute;left:0;top:0;width:1200px;height:8px;background:var(--sky)}
.utility-tab{position:absolute;left:657px;top:0;width:516px;height:71px;background:var(--sky);border-radius:0 0 28px 28px}
.utility-phone{position:absolute;left:14px;top:22px;display:flex;align-items:center;gap:8px;color:var(--ink);font-size:23px}
.utility-divider{position:absolute;left:208px;top:14px;height:44px;border-left:2px dotted rgba(255,255,255,.7)}
.search{position:absolute;left:231px;top:19px;width:272px;height:41px;background:var(--white);border-radius:21px;overflow:hidden}
.search-field{position:absolute;left:21px;top:10px;font-size:16px;color:#8a8f94}
.search-button{position:absolute;right:0;top:0;width:55px;height:41px;background:var(--search-btn);border-radius:0 21px 21px 0;display:flex;align-items:center;justify-content:center}

.brand{position:absolute;left:30px;top:30px;width:240px;height:150px}
.brand-mark{position:absolute;left:80px;top:4px;width:96px;height:96px;border-radius:50%;background:var(--navy)}
.brand-name{position:absolute;left:0;top:118px;font-family:"Noto Serif",Georgia,serif;font-size:24px;letter-spacing:1px;color:#3d4a5a;white-space:nowrap;text-transform:uppercase}

.main-nav{position:absolute;right:27px;top:153px;display:flex;align-items:center;font-family:"Roboto Condensed",Arial,sans-serif;font-size:20px;text-transform:uppercase;color:var(--nav-grey)}
.main-nav .sep{margin:0 14px;font-size:24px;color:#7a828a}
.main-nav .is-active{color:var(--nav-active)}

.hero{position:absolute;left:0;top:204px;width:1200px;height:424px;background:var(--black)}
.hero-visual{position:absolute;left:667px;top:0;width:388px;height:424px;background:radial-gradient(ellipse at 50% 45%,#b49a6a 0%,#5a4f3c 22%,#1e1c1a 48%,#000 72%)}
.hero-copy{position:absolute;left:27px;top:98px;width:440px}
.hero-title{font-family:"Roboto Condensed",Arial,sans-serif;font-weight:700;font-size:45px;line-height:43px;color:var(--sky);text-transform:uppercase}
.hero-text{margin-top:22px;font-size:17.5px;line-height:28.6px;color:var(--white)}
.hero-more{margin-top:16px;display:flex;align-items:center;gap:7px;font-size:18px;font-weight:700;color:var(--sky)}
.slider-dots{position:absolute;left:565px;top:384px;display:flex;gap:7px}
.slider-dots span{width:19px;height:19px;border-radius:50%;background:#8a9299}
.slider-dots .is-current{background:var(--sky)}

.feature-row{position:absolute;left:29px;top:688px;width:1144px;height:297px;display:flex}
.feature{width:286px;height:297px;position:relative;padding:25px 17px 0;color:var(--white)}
.feature--why{background:var(--sky)}
.feature--services{background:var(--navy)}
.feature--news{background:var(--slate)}
.feature--contact{background:var(--charcoal)}
.feature-title{font-family:"Roboto Condensed",Arial,sans-serif;font-weight:400;font-size:29px;line-height:30px;text-transform:uppercase;margin-bottom:7px}
.feature-text{font-size:15.5px;line-height:28.6px}
.link-list{list-style:none;width:250px}
.link-list li{position:relative;padding:4px 0 4px 25px;border-bottom:1px dotted rgba(255,255,255,.55);line-height:27px}
.link-list li:last-child{border-bottom:none}
.link-list li::before{content:"";position:absolute;left:8px;top:14px;border-left:6px solid rgba(255,255,255,.75);border-top:4px solid transparent;border-bottom:4px solid transparent}
.link-list--services li{font-family:"Noto Serif",Georgia,serif;font-size:15.5px;color:var(--sky-light)}
.link-list--news li{font-size:15.5px;color:var(--sky-light);line-height:28.6px;padding:2px 0 4px 25px}
.btn-more{position:absolute;left:17px;top:244px;width:108px;height:30px;background:var(--black);color:var(--white);font-size:15.5px;display:flex;align-items:center;justify-content:center;border-radius:2px}
.contact-lines{font-size:15.5px;line-height:28.6px;margin-top:2px}
.contact-item{display:flex;align-items:center;gap:8px;margin-top:14px;font-size:15.5px}
.contact-item--link{font-family:"Noto Serif",Georgia,serif;color:var(--link-pale)}

.site-footer{position:absolute;left:29px;top:1045px;width:1144px;border-top:1px solid var(--rule)}
.footer-nav{position:absolute;left:0;top:32px;display:flex;align-items:center;font-size:15.5px;color:var(--ink);white-space:nowrap}
.footer-nav .dot{width:8px;height:8px;border-radius:50%;background:var(--sky);margin:0 17px}
.copyright{position:absolute;left:0;top:70px;font-size:14px;color:#555;white-space:nowrap}
.social{position:absolute;right:0;top:36px;display:flex;gap:6px}
.social span{width:54px;height:53px;border-radius:2px}
.social .social-a{background:linear-gradient(#4d6cc0,#2f4a96)}
.social .social-b{background:linear-gradient(#45c4ee,#1fa3d9)}
.social .social-c{background:linear-gradient(#1a7ab8,#0b5a8c)}
</style>
</head>
<body>

<header class="site-header">
  <div class="top-strip"></div>
  <div class="utility-tab">
    <div class="utility-phone">
      <svg width="36" height="26" viewBox="0 0 36 26" aria-hidden="true"><path d="M2 9c0-5 8-7 16-7s16 2 16 7v3h-8V8c-3-1-13-1-16 0v4H2z" fill="#fff"/><path d="M9 12h18l4 12H5z" fill="#fff"/><circle cx="18" cy="18" r="4" fill="#06a6e8"/></svg>
      <span>832-555-0148</span>
    </div>
    <div class="utility-divider"></div>
    <div class="search">
      <span class="search-field">Search</span>
      <span class="search-button"><svg width="22" height="22" viewBox="0 0 22 22" aria-hidden="true"><circle cx="8" cy="8" r="6" fill="none" stroke="#fff" stroke-width="2.5"/><path d="M12.5 12.5l7 7" stroke="#fff" stroke-width="3" stroke-linecap="round"/></svg></span>
    </div>
  </div>

  <a class="brand" href="#">
    <span class="brand-mark"></span>
    <span class="brand-name">Corvel Tindry, PLLC</span>
  </a>

  <nav class="main-nav">
    <a class="is-active" href="#">Home</a><span class="sep">/</span>
    <a href="#">About Us</a><span class="sep">/</span>
    <a href="#">Services</a><span class="sep">/</span>
    <a href="#">Resources</a><span class="sep">/</span>
    <a href="#">Fees</a><span class="sep">/</span>
    <a href="#">Blog</a><span class="sep">/</span>
    <a href="#">Coantact Us</a>
  </nav>
</header>

<section class="hero">
  <div class="hero-visual" role="img" aria-label="Photograph of a glowing light bulb with a brain inside, on a dark background"></div>
  <div class="hero-copy">
    <h1 class="hero-title">Lorem Ipsum is simply dummy</h1>
    <p class="hero-text">Lorem Ipsum has been the industry's standard dummy text ever since the 1500s, when an unknown printer took a galley.</p>
    <a class="hero-more" href="#">Read More
      <svg width="24" height="24" viewBox="0 0 24 24" aria-hidden="true"><circle cx="12" cy="12" r="10" fill="none" stroke="#06a6e8" stroke-width="2"/><path d="M7 12h9M12.5 8l4 4-4 4" fill="none" stroke="#06a6e8" stroke-width="2" stroke-linecap="round" stroke-linejoin="round"/></svg>
    </a>
  </div>
  <div class="slider-dots"><span class="is-current"></span><span></span><span></span></div>
</section>

<main class="feature-row">
  <section class="feature feature--why">
    <h2 class="feature-title">Why Us</h2>
    <p class="feature-text">Lorem Ipsum is simply dummy text of the printing and typesetting industry. Lorem Ipsum has been the industry's standard dummy text ever since the 1500s.</p>
    <a class="btn-more" href="#">Read More</a>
  </section>

  <section class="feature feature--services">
    <h2 class="feature-title">What We Do</h2>
    <ul class="link-list link-list--services">
      <li>Intellectual Property</li>
      <li>Patents</li>
      <li>Copyrights</li>
      <li>Trademarks</li>
      <li>Trade secrets</li>
    </ul>
    <a class="btn-more" href="#">Read More</a>
  </section>

  <section class="feature feature--news">
    <h2 class="feature-title">Latest News</h2>
    <ul class="link-list link-list--news">
      <li>Lorem ipsum dolor sit amet, consectetur adipiscing elit.</li>
      <li>In posuere turpis quis molestie tempus.</li>
      <li>Integer sit amet lacus porta.</li>
    </ul>
    <a class="btn-more" href="#">Read More</a>
  </section>

  <section class="feature feature--contact">
    <h2 class="feature-title">Contact Info</h2>
    <p class="contact-lines">Lorenz T. Abery<br>48 Larkspur Row<br>Houston, TX 77002</p>
    <p class="contact-item">
      <svg width="14" height="24" viewBox="0 0 14 24" aria-hidden="true"><rect x="1" y="1" width="12" height="22" rx="2" fill="none" stroke="#fff" stroke-width="2"/><rect x="3" y="4" width="8" height="13" fill="#fff"/></svg>
      <span>832-555-0148</span>
    </p>
    <p class="contact-item contact-item--link">
      <svg width="22" height="15" viewBox="0 0 22 15" aria-hidden="true"><rect x="1" y="1" width="20" height="13" fill="none" stroke="#fff" stroke-width="1.6"/><path d="M1 1l10 8 10-8M1 14l7-6M21 14l-7-6" fill="none" stroke="#fff" stroke-width="1.4"/></svg>
      <span>info@corveltindry.example</span>
    </p>
    <p class="contact-item contact-item--link">
      <svg width="18" height="24" viewBox="0 0 18 24" aria-hidden="true"><path d="M9 1a8 8 0 0 0-8 8c0 6 8 14 8 14s8-8 8-14a8 8 0 0 0-8-8z" fill="#fff"/><circle cx="9" cy="9" r="3" fill="#44525c"/></svg>
      <span>Location Map</span>
    </p>
  </section>
</main>

<footer class="site-footer">
  <nav class="footer-nav">
    <a href="#">Home</a><span class="dot"></span>
    <a href="#">About Us</a><span class="dot"></span>
    <a href="#">Services</a><span class="dot"></span>
    <a href="#">Resources</a><span class="dot"></span>
    <a href="#">Fees</a><span class="dot"></span>
    <a href="#">Blog</a><span class="dot"></span>
    <a href="#">Coantact Us</a>
  </nav>
  <p class="copyright">Copyright © 2014, Corvel Tindry, PLLC. All rights reserverd</p>
  <div class="social">
    <span class="social-a" role="img" aria-label="Social network link"></span>
    <span class="social-b" role="img" aria-label="Social network link"></span>
    <span class="social-c" role="img" aria-label="Professional network link"></span>
  </div>
</footer>

</body>
</html>
```